Business Card Design needed for logo design project

Our company needs a Business Card Design. Please refer to our original project in the link above.
Dorian Pellworth
Broker

W: Velvetcrestestates.example
P: 555-302-7184
F: 555-741-2096
E: dorianpellworth@mailbox.example
A: North Dallas Office
Updates

Name Spelling update , sorry Dorian Pellworth card is double sided

```html
<!DOCTYPE html>
<html lang="en">
<head>
<meta charset="utf-8">
<title>Dorian Pellworth – Business Card</title>
<link rel="stylesheet" href="https://fonts.googleapis.com/css2?family=Arimo:wght@400;700&family=Cinzel:wght@500&display=swap">
<style>
  :root {
    --backdrop: #c0a063;
    --wood-dark: #4a2818;
    --wood-mid: #6a3d28;
    --wood-light: #7a4a32;
    --card-white: #ffffff;
    --ink: #231f20;
    --gold: #b89a62;
    --gold-bright: #c9a86a;
  }
  html, body {
    margin: 0;
    padding: 0;
    width: 1200px;
    height: 1000px;
    overflow: hidden;
    background: var(--backdrop);
  }
  .canvas {
    position: relative;
    width: 1200px;
    height: 1000px;
    background: var(--backdrop);
  }
  .card {
    position: absolute;
    left: 243px;
    width: 715px;
    height: 380px;
    overflow: hidden;
  }
  .card-front {
    top: 82px;
    background: var(--wood-mid);
  }
  .wood-surface {
    position: absolute;
    inset: 0;
    background: linear-gradient(175deg, var(--wood-light) 0%, var(--wood-mid) 45%, var(--wood-dark) 100%);
  }
  .front-brand {
    position: absolute;
    left: 0;
    right: 0;
    top: 150px;
    text-align: center;
  }
  .brand-dot {
    display: block;
    width: 70px;
    height: 70px;
    margin: 0 auto 28px;
    border-radius: 50%;
    background: var(--gold-bright);
  }
  .brand-name {
    font-family: "Cinzel", serif;
    font-weight: 500;
    font-size: 26px;
    letter-spacing: 1px;
    color: var(--gold-bright);
  }
  .card-back {
    top: 537px;
    background: var(--card-white);
    font-family: "Arimo", Arial, sans-serif;
    color: var(--ink);
  }
  .person-name {
    position: absolute;
    left: 45px;
    top: 66px;
    margin: 0;
    font-size: 47px;
    font-weight: 700;
    line-height: 1;
  }
  .person-role {
    position: absolute;
    left: 45px;
    top: 144px;
    margin: 0;
    font-size: 44px;
    font-weight: 400;
    line-height: 1;
  }
  .back-brand {
    position: absolute;
    left: 520px;
    top: 44px;
    width: 150px;
    text-align: center;
  }
  .back-brand .brand-dot {
    width: 52px;
    height: 52px;
    margin-bottom: 8px;
    background: var(--gold);
  }
  .back-brand .brand-name {
    font-size: 13px;
    color: var(--gold);
    letter-spacing: 0.5px;
  }
  .website {
    position: absolute;
    left: 333px;
    top: 161px;
    font-size: 26px;
    color: var(--gold);
    line-height: 1;
  }
  .contact-list {
    position: absolute;
    left: 45px;
    top: 240px;
    margin: 0;
    padding: 0;
    list-style: none;
    font-size: 26px;
    line-height: 32px;
  }
</style>
</head>
<body>
  <main class="canvas">
    <section class="card card-front">
      <div class="wood-surface" role="img" aria-label="Dark walnut wood grain texture"></div>
      <div class="front-brand">
        <span class="brand-dot"></span>
        <span class="brand-name">Velvetcrest Estates Realty</span>
      </div>
    </section>

    <section class="card card-back">
      <h1 class="person-name">Dorian Pellworth</h1>
      <p class="person-role">Broker</p>
      <div class="back-brand">
        <span class="brand-dot"></span>
        <span class="brand-name">Velvetcrest Estates</span>
      </div>
      <div class="website">Velvetcrestestates.example</div>
      <ul class="contact-list">
        <li>P: 555-302-7184</li>
        <li>F: 555-741-2096</li>
        <li>E: dorianpellworth@mailbox.example</li>
      </ul>
    </section>
  </main>
</body>
</html>
```